Business Card for Technology Startup

Design a 2-sided business card using the logo provided. We are a digital healthcare platform that provides a mobile app and web UI that helps caregivers, families, and doctors share information and provide better patient outcomes. We use AI and machine learning to help guide patients through their day-to-day life. The final design should communicate stability, peace, comfort, but also align with the image of an AI-driven technology startup.

I'd like the deliverable to by a Photoshop PSD file (with layers) that I can work with in pixlr.com. Should contain the following editable layers:
Name (ex. Elin Vore)
Title (ex. Founder / CEO)
Email (ex. info@brenvaxa.ai)
Phone (ex. (555) 214-7083)
Website (ex. https://brenvaxa.ai)

```html
<!DOCTYPE html>
<html lang="en">
<head>
<meta charset="utf-8">
<title>Brenvaxa Business Card</title>
<link rel="stylesheet" href="https://fonts.googleapis.com/css2?family=Montserrat:wght@400;700;800&display=swap">
<style>
  :root {
    --canvas: #2a2a2a;
    --card: #161616;
    --cyan: #13bde9;
    --cyan-soft: #6fd0e3;
    --white: #ffffff;
    --muted: #e9e9e9;
  }
  * { box-sizing: border-box; margin: 0; padding: 0; }
  html, body { width: 1200px; height: 689px; overflow: hidden; }
  body {
    background: var(--canvas);
    font-family: "Montserrat", Arial, sans-serif;
    display: flex;
    align-items: center;
    justify-content: center;
    gap: 48px;
  }
  .card {
    width: 530px;
    height: 303px;
    background: var(--card);
    border-radius: 20px;
    position: relative;
    box-shadow: 0 18px 40px rgba(0,0,0,0.45);
    overflow: hidden;
  }

  /* Front side */
  .card-front {
    display: flex;
    align-items: center;
    justify-content: center;
    gap: 18px;
  }
  .front-dot {
    width: 64px;
    height: 64px;
    border-radius: 50%;
    background: linear-gradient(135deg, var(--cyan), var(--cyan-soft));
    flex: none;
  }
  .front-name {
    color: var(--cyan);
    font-weight: 800;
    font-size: 54px;
    letter-spacing: 0.5px;
    white-space: nowrap;
  }

  /* Back side */
  .card-back {
    display: flex;
    align-items: center;
    padding: 0 34px 0 40px;
  }
  .brand {
    display: flex;
    align-items: center;
    gap: 10px;
    width: 210px;
    flex: none;
  }
  .brand-dot {
    width: 18px;
    height: 18px;
    border-radius: 50%;
    background: var(--cyan);
    flex: none;
  }
  .brand-name {
    color: var(--white);
    font-weight: 800;
    font-size: 33px;
    letter-spacing: 0.3px;
    white-space: nowrap;
  }
  .divider {
    width: 1.5px;
    height: 150px;
    background: var(--cyan);
    margin: 0 26px 0 12px;
    flex: none;
  }
  .details { display: flex; flex-direction: column; }
  .person-name {
    color: var(--cyan-soft);
    font-weight: 800;
    font-size: 27px;
    line-height: 1.05;
    white-space: nowrap;
  }
  .person-title {
    color: var(--muted);
    font-weight: 400;
    font-size: 14px;
    margin-top: 3px;
  }
  .contacts {
    list-style: none;
    margin-top: 22px;
    display: flex;
    flex-direction: column;
    gap: 6px;
  }
  .contact {
    display: flex;
    align-items: center;
    gap: 8px;
    color: var(--muted);
    font-size: 13px;
    white-space: nowrap;
  }
  .contact-icon { width: 11px; height: 11px; flex: none; fill: var(--cyan); }
</style>
</head>
<body>
  <section class="card card-front" aria-label="Business card front">
    <span class="front-dot"></span>
    <span class="front-name">brenvaxa</span>
  </section>

  <section class="card card-back" aria-label="Business card back">
    <div class="brand">
      <span class="brand-dot"></span>
      <span class="brand-name">brenvaxa</span>
    </div>
    <div class="divider"></div>
    <div class="details">
      <h1 class="person-name">Elin Vore</h1>
      <p class="person-title">Founder / CEO</p>
      <ul class="contacts">
        <li class="contact">
          <svg class="contact-icon" viewBox="0 0 12 12"><path d="M0 2h12v8H0z" fill="var(--cyan)"/><path d="M0.6 2.4l5.4 4 5.4-4" fill="none" stroke="#161616" stroke-width="1"/></svg>
          <span>info@brenvaxa.ai</span>
        </li>
        <li class="contact">
          <svg class="contact-icon" viewBox="0 0 12 12"><path d="M2.4 0.8l2 2.2-1.1 1.3c.7 1.6 2 2.9 3.5 3.6l1.3-1.1 2.2 2-1 2c-4.6-.5-8.2-4.1-8.7-8.7z"/></svg>
          <span>(555) 214-7083</span>
        </li>
        <li class="contact">
          <svg class="contact-icon" viewBox="0 0 12 12"><circle cx="6" cy="6" r="5.3" fill="none" stroke="var(--cyan)" stroke-width="1.3"/><path d="M0.7 6h10.6M6 0.7c-2.6 3-2.6 7.6 0 10.6M6 0.7c2.6 3 2.6 7.6 0 10.6" fill="none" stroke="var(--cyan)" stroke-width="1"/></svg>
          <span>https://brenvaxa.ai</span>
        </li>
      </ul>
    </div>
  </section>
</body>
</html>
```